Catalogue Design Project

We require a new 2013 catalogue cover designed ( front & back with a one inch wide spine) for our business, Brellow Office Supplies. We have been established for 36 years and we supply all sorts of companies across the UK with a Variety of Office Stationery, Computer Products, Print, Furniture, Catering and Cleaning products within the UK - you can browse our catalogue on our website www.brellow.co.uk - using test as both user id and password.
We are serious about customer service; ensure we do the very best for our clients with the best prices. For us it’s all about the image we portray to our clients, we don’t want the cover to look like it’s the cover of a Yacht catalogue, nor do we want it to look like a trashy magazine.
The main priority of this design is that the Catalogue looks professional and appealing. Good use of colour, possibly incorporating elements of what we do would be of advantage.
(Please visit our website www.brellow.co.uk for details).
The Catalogue is to be A4 in size, MUST have our company logo in on the front, which we will supply, but for the start obtainable from our site)
The Catalogue covers will have insides both front and back that we will be printing on. Your design and use of colours should be able to flow onto these pages so as we can print on a continuation of your design.
**UPDATE - Please note the content is already designed, this is for the front/back cover and inside covers**
There will be a few edits after we make a choice...
if you need anything from us then please email us on jpike@brellow.co.uk
Best of luck
PROJECT NOW GUARANTEED.!!
Due to the High Quality of designs being submitted - we are now happy to commit to one of you! Keep the designs coming!
Good Luck!
The Buyers of our products are corporate companies
Printing

```html
<!DOCTYPE html>
<html lang="en">
<head>
<meta charset="utf-8">
<title>Brellow Office Supplies – 2013 Catalogue Cover</title>
<link rel="stylesheet" href="https://fonts.googleapis.com/css2?family=Courier+Prime:ital,wght@0,400;0,700;1,400;1,700&display=swap">
<style>
  :root {
    --amber: #f8b012;
    --amber-light: #ffe08a;
    --amber-deep: #f2a20c;
    --art-tone: #c48a35;
    --band: rgba(255, 240, 200, 0.32);
    --ink: #111111;
    --ink-soft: #3a3a3a;
    --gold: #c9a400;
    --sticker: #f4f4f4;
    --sticker-fold: #d6d6d6;
    --sticker-text: #9a9a9a;
    --star: #f3a316;
    --paper: #ffffff;
  }
  * { margin: 0; padding: 0; box-sizing: border-box; }
  html, body { width: 882px; height: 1200px; overflow: hidden; }
  body { font-family: "Courier Prime", "Courier New", monospace; }

  .cover {
    position: relative;
    width: 882px;
    height: 1200px;
    overflow: hidden;
    background:
      radial-gradient(ellipse 520px 560px at 300px 520px, var(--amber-light) 0%, rgba(255,224,138,0) 75%),
      linear-gradient(180deg, var(--amber) 0%, var(--amber-deep) 100%);
  }

  .pencil-area {
    position: absolute;
    left: 240px; top: 0;
    width: 642px; height: 1150px;
    background: linear-gradient(200deg, rgba(196,138,53,0.10) 0%, rgba(196,138,53,0.28) 100%);
  }

  .category-band { position: absolute; background: var(--band); }
  .category-band--right { left: 497px; top: 611px; width: 385px; height: 296px; }
  .category-band--left  { left: 0; top: 714px; width: 497px; height: 193px; }

  .edition-sticker { position: absolute; left: 72px; top: 38px; width: 220px; height: 220px; }

  .brand-card {
    position: absolute;
    left: 11px; top: 552px;
    width: 483px; height: 138px;
    background: var(--paper);
    border-radius: 6px;
    box-shadow: 0 3px 8px rgba(0,0,0,0.35);
    display: flex;
    flex-direction: column;
    align-items: flex-end;
    justify-content: center;
    padding-right: 22px;
    color: var(--gold);
    font-weight: 400;
  }
  .brand-card__name { font-size: 64px; letter-spacing: 8px; line-height: 1; margin-right: -8px; }
  .brand-card__tagline { font-size: 24px; margin-top: 6px; }

  .range { position: absolute; color: var(--ink); white-space: nowrap; line-height: 1; }
  .range--bold { font-weight: 700; }
  .range--italic { font-style: italic; }

  .range--furniture   { left: 35px; top: 736px; font-size: 35px; letter-spacing: 9px; }
  .range--seating     { left: 38px; top: 777px; font-size: 34px; letter-spacing: 22px; }
  .range--machines    { left: 35px; top: 820px; font-size: 44px; letter-spacing: 4px; }
  .range--consumables { left: 35px; top: 866px; font-size: 36px; letter-spacing: 10px; }

  .range--vertical { transform-origin: 0 0; transform: rotate(90deg); }
  .range--print { left: 554px; top: 620px; font-size: 48px; letter-spacing: 12px; }
  .range--legal { left: 590px; top: 614px; font-size: 28px; letter-spacing: 3px; color: var(--ink-soft); }

  .range--office     { left: 606px; top: 612px; font-size: 62px; letter-spacing: 5px; }
  .range--stationary { left: 610px; top: 674px; font-size: 36px; letter-spacing: 3px; color: var(--ink-soft); }
  .range--product    { left: 601px; top: 720px; font-size: 44px; letter-spacing: 11px; color: var(--ink-soft); }
  .range--sourcing   { left: 601px; top: 758px; font-size: 44px; letter-spacing: 6px; color: var(--ink-soft); }
  .range--facilities { left: 599px; top: 806px; font-size: 40px; letter-spacing: 2px; }
  .range--management { left: 599px; top: 843px; font-size: 40px; letter-spacing: 2px; color: var(--ink-soft); }
  .range--catering   { left: 600px; top: 877px; font-size: 24px; letter-spacing: 7px; color: var(--ink-soft); }
</style>
</head>
<body>
<main class="cover">

  <div class="pencil-area" role="img" aria-label="Illustration of a large pencil sweeping diagonally down the cover, its tip drawing a line"></div>

  <div class="category-band category-band--right"></div>
  <div class="category-band category-band--left"></div>

  <svg class="edition-sticker" viewBox="0 0 220 220" aria-label="New 2013 edition">
    <circle cx="110" cy="110" r="100" fill="var(--sticker)"/>
    <path d="M 150 20 A 100 100 0 0 1 205 80 L 150 80 Z" fill="var(--sticker-fold)"/>
    <g transform="rotate(40 110 110)" fill="var(--sticker-text)" text-anchor="middle"
       font-family="Courier Prime, Courier New, monospace">
      <text x="110" y="78" font-size="44">NEW</text>
      <text x="110" y="130" font-size="46">2013</text>
      <text x="110" y="158" font-size="20" letter-spacing="2">EDITION</text>
    </g>
    <polygon points="32,80 36,92 48,92 38,99 42,111 32,104 22,111 26,99 16,92 28,92" fill="var(--star)"/>
    <polygon points="140,168 144,180 156,180 146,187 150,199 140,192 130,199 134,187 124,180 136,180" fill="var(--star)"/>
  </svg>

  <div class="brand-card">
    <span class="brand-card__name">BRELLOW</span>
    <span class="brand-card__tagline">Office Supplies</span>
  </div>

  <p class="range range--bold range--furniture">OFFICE FURNITURE</p>
  <p class="range range--italic range--seating">AND SEATING</p>
  <p class="range range--italic range--machines">BUSINESS MACHINES</p>
  <p class="range range--bold range--consumables">&amp; IT CONSUMABLES</p>

  <p class="range range--bold range--vertical range--print">PRINT</p>
  <p class="range range--vertical range--legal">LEGAL SUPPLIES</p>

  <p class="range range--office">OFFICE</p>
  <p class="range range--stationary">STATIONARY</p>
  <p class="range range--italic range--product">PRODUCT</p>
  <p class="range range--italic range--sourcing">SOURCING</p>
  <p class="range range--bold range--italic range--facilities">FACILITIES</p>
  <p class="range range--italic range--management">MANAGEMENT</p>
  <p class="range range--catering">AND CATERING</p>

</main>
</body>
</html>
```